Cedarline Joinery eye catching business card

I need an eye catching business card that reflects my traditional, fun, handmade woodcraft shop. I make high end custom furniture and fine woodworking products, a lot of which are rustic, natural looking. We are a small shop but we produce awesome, one of a kind wood products, and our business card should reflect that. Our target audience is young professionals to retired folks who want a quality, local, handmade product. I'd like the Shop Nearby logo somewhere on the card, BUT not overwhelming, the main focus is my Logo, no preference on color whichever looks the best. Visit my website to get a feel for my company. Cedarlinejoinery.com
Target Market(s)
young professionals to retired folks. Any one who wants to furnish their home with quality handcrafted products.
Industry/Entity Type
Business
Contact Information for Business Card
Marlo Finch (555)417-6382
marlo@cedarlinejoinery.com
www.cedarlinejoinery.com
Look and feel

```html
<!DOCTYPE html>
<html lang="en">
<head>
<meta charset="utf-8">
<title>Cedarline Joinery – Business Card</title>
<link href="https://fonts.googleapis.com/css2?family=Josefin+Sans:wght@400;700&family=Roboto+Slab:wght@800&display=swap" rel="stylesheet">
<style>
  :root{
    --backdrop:#d8d8d8;
    --ink:#1b1b1b;
    --charcoal:#262626;
    --photo-dark:#141414;
    --photo-warm:#3a322a;
    --paper:#ffffff;
    --band:#6d6d6d;
    --text-light:#f2f2f2;
  }
  *{margin:0;padding:0;box-sizing:border-box}
  html,body{width:1200px;height:852px;overflow:hidden}
  body{
    background:var(--backdrop);
    font-family:"Josefin Sans",sans-serif;
    position:relative;
  }
  .card{
    position:absolute;
    top:281px;
    width:500px;
    height:290px;
    border-radius:22px;
    overflow:hidden;
    box-shadow:0 6px 18px rgba(0,0,0,.25);
  }
  .card--front{left:70px}
  .card--back{left:630px;background:var(--paper)}

  .workshop-photo{
    position:absolute;inset:0;
    background:radial-gradient(ellipse at 35% 65%,var(--photo-warm) 0%,var(--charcoal) 45%,var(--photo-dark) 100%);
  }

  .brand{
    position:absolute;
    display:flex;flex-direction:column;align-items:center;
  }
  .brand__name{
    font-family:"Roboto Slab",serif;
    font-weight:800;
    letter-spacing:2px;
    text-transform:uppercase;
    line-height:1;
  }
  .brand__tagline{
    font-weight:700;
    text-transform:uppercase;
    letter-spacing:1.5px;
    font-size:9px;
    margin-top:12px;
  }
  .card--front .brand{left:0;right:0;top:108px}
  .card--front .brand__name{color:var(--text-light);font-size:40px}
  .card--front .brand__tagline{color:var(--text-light)}

  .card--back .brand{right:36px;top:48px}
  .card--back .brand__name{color:var(--ink);font-size:30px}
  .card--back .brand__tagline{color:var(--ink);font-size:8px}

  .back-shape{position:absolute;inset:0}
  .back-photo{
    position:absolute;inset:0;
    clip-path:path("M0,150 Q210,200 500,115 V290 H0 Z");
  }

  .contact{
    position:absolute;left:36px;bottom:24px;
    color:var(--text-light);
  }
  .contact__name{font-size:17px;font-weight:700}
  .contact__role{font-size:12px;margin-top:2px;margin-bottom:10px}
  .contact__list{list-style:none;margin-left:18px}
  .contact__item{display:flex;align-items:center;gap:10px;font-size:12.5px;line-height:19px}
  .contact__icon{width:11px;height:11px;fill:var(--text-light)}
</style>
</head>
<body>

<section class="card card--front">
  <div class="workshop-photo" role="img" aria-label="Dimmed photo of a woodworker at a workshop bench"></div>
  <div class="brand">
    <span class="brand__name">Cedarline Joinery</span>
    <span class="brand__tagline">Handmade in Ashford Bay</span>
  </div>
</section>

<section class="card card--back">
  <div class="workshop-photo back-photo" role="img" aria-label="Dimmed photo of workshop tools and a bench"></div>
  <svg class="back-shape" viewBox="0 0 500 290" width="500" height="290">
    <path d="M0,150 Q210,200 500,115 L500,104 Q210,188 0,140 Z" fill="var(--band)"/>
    <path d="M0,0 H500 V104 Q210,188 0,140 Z" fill="var(--paper)"/>
  </svg>
  <div class="brand">
    <span class="brand__name">Cedarline Joinery</span>
    <span class="brand__tagline">Handmade in Ashford Bay</span>
  </div>
  <div class="contact">
    <p class="contact__name">Marlo Finch</p>
    <p class="contact__role">Owner</p>
    <ul class="contact__list">
      <li class="contact__item">
        <svg class="contact__icon" viewBox="0 0 12 12"><path d="M2.5 1 L4.5 1 L5 3.5 L3.8 4.5 Q5 7 7.5 8.2 L8.5 7 L11 7.5 L11 9.5 Q11 11 9.5 11 Q1 10 1 2.5 Q1 1 2.5 1 Z"/></svg>
        <span>(555)417-6382</span>
      </li>
      <li class="contact__item">
        <svg class="contact__icon" viewBox="0 0 12 12"><circle cx="6" cy="6" r="5" fill="none" stroke="var(--text-light)" stroke-width="1.2"/><ellipse cx="6" cy="6" rx="2.2" ry="5" fill="none" stroke="var(--text-light)" stroke-width="1"/><line x1="1" y1="6" x2="11" y2="6" stroke="var(--text-light)" stroke-width="1"/></svg>
        <span>www.cedarlinejoinery.com</span>
      </li>
      <li class="contact__item">
        <svg class="contact__icon" viewBox="0 0 12 12"><rect x="0.5" y="2" width="11" height="8" rx="1"/><path d="M1 2.5 L6 6.5 L11 2.5" fill="none" stroke="var(--charcoal)" stroke-width="1"/></svg>
        <span>marlo@cedarlinejoinery.com</span>
      </li>
    </ul>
  </div>
</section>

</body>
</html>
```